Fern Hollow Academy business card

we need to incorporate our school logo, name, address onto a great new school business card for all our staff - I included a lot of detail below under must haves and I included 3 business card samples below also that give a flavour of what I want - I would like to include a great graphic on at least one side of the card that represents education -

Target Market(s)

this business card will need to be attractive to parents of all ages but especially millennial parents and even high school students who may influence parents to chose Fern Hollow Academy

Industry/Entity Type

Education

Contact Information for Business Card

should contain core value words "excellence service family belief"
will need out school name, Fern Hollow Academy to be present, address 7281 Tamsworth Road, Burnaby, British Columbia V3K1P8
telephone 604.719.2083 Ext. 317
first card will need my name on it, Morvena Pelchuk, Director of Development & Operations
also web address of fernhollowacademy.ca

Font styles to use
Other font styles liked:
• Tw Cent MT

Requirements
Must have
• a fresh modern look for a private school environment that appeals to parents looking for great education - must use school logo, and incorporate colours navy blue, CMYK 100, 60, 0, 56 and burgundy CMYK 27, 98, 81, 50
• below I uploaded 3 business card layouts that look interesting to me - I'd like to incorporate some great school photos into the design - I tried to upload some school photos that we have, that the files are too large apparently? so I could send a link to Filecrate or something like that to share great high res pics that would look nice - we are kindergarten to Gr. 12 school, so I would like to include images that would represent great education at any age.
Nice to have
• spot colour would be nice as an option for printing for maybe key administrator business cards, while the rest would be basic printing

```html
<!DOCTYPE html>
<html lang="en">
<head>
<meta charset="utf-8">
<title>Fern Hollow Academy – Business Card</title>
<link rel="stylesheet" href="https://fonts.googleapis.com/css2?family=Jost:wght@400;500;700&display=swap">
<style>
  :root {
    --navy: #13386b;
    --burgundy: #6b0d14;
    --sky: #29a6df;
    --white: #ffffff;
    --stage: #2b2b2b;
    --text-font: "Jost", sans-serif;
  }
  * { box-sizing: border-box; margin: 0; padding: 0; }
  html, body {
    width: 1200px; height: 900px; overflow: hidden;
    background: var(--stage);
    font-family: var(--text-font);
  }
  .card {
    position: absolute; left: 250px;
    width: 700px; height: 400px;
    background: var(--white);
    overflow: hidden;
  }
  .card--front { top: 35px; }
  .card--back  { top: 465px; }
  .card__art { position: absolute; inset: 0; width: 700px; height: 400px; }

  .brand {
    position: absolute; display: flex; align-items: center; gap: 12px;
  }
  .brand__dot {
    width: 46px; height: 46px; border-radius: 50%;
    background: var(--navy);
  }
  .brand__name {
    color: var(--burgundy); font-weight: 700;
    font-size: 24px; line-height: 0.95; text-transform: uppercase;
  }
  .card--front .brand { left: 58px; top: 40px; }

  .person { position: absolute; left: 110px; top: 140px; }
  .person__name { font-size: 27px; line-height: 1; color: var(--burgundy); letter-spacing: 0.5px; }
  .person__name strong { color: var(--navy); font-weight: 700; }
  .person__title { font-size: 16px; color: var(--navy); font-weight: 500; margin-top: 3px; }

  .contact {
    position: absolute; left: 110px;
    font-size: 17px; font-weight: 500; color: var(--navy);
  }
  .contact--phone { top: 214px; }
  .contact--web { top: 264px; }
  .contact--address { top: 318px; color: var(--white); font-weight: 400; font-size: 18px; line-height: 1.35; }

  .card--back .brand-box {
    position: absolute; left: 420px; top: 172px;
    width: 146px; height: 116px;
    background: var(--white); border: 2px solid var(--navy);
    display: flex; align-items: center; justify-content: center;
  }
  .card--back .brand-box .brand__name { font-size: 20px; text-align: left; }

  .values {
    position: absolute; left: 588px; top: 218px;
    font-weight: 700; font-size: 15px; line-height: 1.05; text-transform: uppercase;
  }
  .values__main { color: var(--burgundy); }
  .values__accent { color: var(--sky); }
</style>
</head>
<body>

<section class="card card--front">
  <svg class="card__art" viewBox="0 0 700 400" aria-hidden="false">
    <polygon points="0,292 385,292 480,400 0,400" fill="var(--navy)"/>
    <polygon points="480,0 650,0 610,40 445,40" fill="var(--navy)"/>
    <polygon points="570,300 700,220 700,330 610,360" fill="var(--navy)"/>
    <polygon points="430,150 600,10 700,130 540,300" fill="var(--burgundy)"/>
    <defs>
      <linearGradient id="danceGlow" x1="0" y1="0" x2="1" y2="1">
        <stop offset="0" stop-color="#e0391c"/>
        <stop offset="1" stop-color="#b82510"/>
      </linearGradient>
    </defs>
    <rect x="470" y="38" width="190" height="220" fill="url(#danceGlow)" role="img"
      aria-label="Photo of students performing a dance lift against a red backdrop"/>
    <g fill="none" stroke="var(--burgundy)" stroke-width="2">
      <circle cx="68" cy="160" r="13"/>
      <circle cx="68" cy="226" r="13"/>
      <circle cx="68" cy="276" r="13"/>
    </g>
    <g fill="var(--burgundy)">
      <circle cx="68" cy="156" r="4"/>
      <path d="M60 167 a8 7 0 0 1 16 0 z"/>
      <path d="M62 220 l4 -1 2 5 -2 2 a10 10 0 0 0 5 5 l2 -2 5 2 -1 4 a3 3 0 0 1 -3 2 a15 15 0 0 1 -14 -14 a3 3 0 0 1 2 -3 z"/>
    </g>
    <g fill="none" stroke="var(--burgundy)" stroke-width="1.4">
      <circle cx="68" cy="276" r="7"/>
      <ellipse cx="68" cy="276" rx="3" ry="7"/>
      <line x1="61" y1="276" x2="75" y2="276"/>
    </g>
    <circle cx="68" cy="343" r="15" fill="none" stroke="var(--white)" stroke-width="2"/>
    <path d="M68 353 l-6 -9 a7 7 0 1 1 12 0 z" fill="var(--white)"/>
    <circle cx="68" cy="339" r="2.5" fill="var(--navy)"/>
  </svg>

  <div class="brand">
    <span class="brand__dot"></span>
    <span class="brand__name">Fern Hollow<br>Academy</span>
  </div>

  <div class="person">
    <p class="person__name">MORVENA <strong>PELCHUK</strong></p>
    <p class="person__title">Director of Development &amp; Operations</p>
  </div>
  <p class="contact contact--phone">604.719.2083 Ext. 317</p>
  <p class="contact contact--web">fernhollowacademy.ca</p>
  <p class="contact contact--address">7281 Tamsworth Road, Burnaby,<br>British Columbia V3K1P8</p>
</section>

<section class="card card--back">
  <svg class="card__art" viewBox="0 0 700 400">
    <polygon points="0,0 220,0 0,140" fill="var(--navy)"/>
    <polygon points="0,140 150,50 150,400 0,400" fill="var(--burgundy)"/>
    <polygon points="220,70 480,70 480,250 220,250" fill="var(--burgundy)"/>
    <polygon points="150,50 220,50 220,250 150,400" fill="var(--white)"/>
    <defs>
      <linearGradient id="gradGlow" x1="0" y1="0" x2="1" y2="0">
        <stop offset="0" stop-color="#8b1a1a"/>
        <stop offset="0.5" stop-color="#3a2a28"/>
        <stop offset="1" stop-color="#1e2a22"/>
      </linearGradient>
    </defs>
    <rect x="170" y="40" width="280" height="185" fill="url(#gradGlow)" role="img"
      aria-label="Photo of graduating students in caps and gowns"/>
  </svg>

  <div class="brand-box">
    <span class="brand__name">Fern Hollow<br>Academy</span>
  </div>

  <p class="values">
    <span class="values__main">Excellence</span> <span class="values__accent">Service</span><br>
    <span class="values__accent">Family Belief</span>
  </p>
</section>

</body>
</html>
```